Real Estate Investing company needs a business card design

We need a business card design for new Real Estate Investment Company called "Brightgate Holdings, LLC." We buy homes for cash and close quickly in any situation. Our company provides an easy and fast option for home owners who are in tough situations who need to sell their home fast and don't want realtor fees or other listing hassles. We also renovate and resell our homes which helps provide housing for the community. We would like to see designs that use the colors blue and white to match our company logo or other colors that may match our company logo. The final design should communicate trust and easy process.
Industry/Entity Type
Business
Contact Information for Business Card
Front should have company name and company logo. back of card should have company logo and area to list services.
Look and feel

```html
<!DOCTYPE html>
<html lang="en">
<head>
<meta charset="utf-8">
<title>Brightgate Holdings — Business Card</title>
<link rel="stylesheet" href="https://fonts.googleapis.com/css2?family=Exo+2:wght@500;700&display=swap">
<style>
  :root {
    --page: #ffffff;
    --card-blue: #0f72b9;
    --ink-white: #ffffff;
    --band-light: rgba(255, 255, 255, 0.22);
  }
  html, body {
    margin: 0;
    padding: 0;
    width: 1200px;
    height: 1200px;
    overflow: hidden;
    background: var(--page);
  }
  .canvas {
    position: relative;
    width: 1200px;
    height: 1200px;
  }
  .card {
    position: absolute;
    left: 318px;
    width: 556px;
    height: 361px;
    background: var(--card-blue);
    overflow: hidden;
  }
  .card--front { top: 213px; }
  .card--back { top: 592px; }
  .light-band {
    position: absolute;
    left: 0;
    width: 556px;
    height: 84px;
    background:
      linear-gradient(to bottom, transparent 0%, var(--band-light) 30%, var(--band-light) 70%, transparent 100%);
    -webkit-mask-image: linear-gradient(to right, #000 0%, rgba(0,0,0,0.35) 50%, #000 100%);
    mask-image: linear-gradient(to right, #000 0%, rgba(0,0,0,0.35) 50%, #000 100%);
  }
  .card--front .light-band { top: 140px; }
  .card--back .light-band { top: 130px; }
  .brand-name {
    position: absolute;
    display: flex;
    align-items: center;
    gap: 8px;
    font-family: "Exo 2", sans-serif;
    font-weight: 700;
    color: var(--ink-white);
    text-transform: uppercase;
    line-height: 1;
    transform: translate(-50%, -50%);
    white-space: nowrap;
  }
  .brand-name__mark {
    width: 14px;
    height: 14px;
    background: var(--ink-white);
    flex: none;
  }
  .brand-name__text {
    display: flex;
    flex-direction: column;
    gap: 3px;
  }
  .card--front .brand-name {
    left: 286px;
    top: 171px;
    font-size: 28px;
  }
  .card--back .brand-name {
    left: 423px;
    top: 168px;
    font-size: 23px;
  }
  .services-divider {
    position: absolute;
    left: 300px;
    top: 61px;
    width: 1px;
    height: 229px;
    background: var(--ink-white);
    opacity: 0.85;
  }
  .services {
    position: absolute;
    left: 40px;
    top: 82px;
    width: 230px;
    font-family: "Exo 2", sans-serif;
    color: var(--ink-white);
  }
  .services__title {
    margin: 0 0 16px;
    font-size: 18px;
    font-weight: 700;
    text-transform: uppercase;
    letter-spacing: 0.5px;
  }
  .services__list {
    margin: 0;
    padding: 0;
    list-style: none;
    font-size: 15px;
    font-weight: 500;
    line-height: 1;
  }
  .services__item {
    display: flex;
    align-items: center;
    gap: 10px;
    margin-bottom: 18px;
  }
  .services__tick {
    width: 14px;
    height: 14px;
    flex: none;
  }
</style>
</head>
<body>
<main class="canvas">

  <section class="card card--front" aria-label="Card front">
    <div class="light-band" role="img" aria-label="Soft white light band across the card"></div>
    <div class="brand-name">
      <span class="brand-name__mark"></span>
      <span class="brand-name__text"><span>Brightgate</span><span>Holdings</span></span>
    </div>
  </section>

  <section class="card card--back" aria-label="Card back">
    <div class="light-band" role="img" aria-label="Soft white light band across the card"></div>
    <div class="services">
      <h2 class="services__title">Our Services</h2>
      <ul class="services__list">
        <li class="services__item"><svg class="services__tick" viewBox="0 0 14 14" aria-hidden="true"><path d="M2 7.5 L5.5 11 L12 3.5" fill="none" stroke="#fff" stroke-width="2"/></svg>Cash Home Purchases</li>
        <li class="services__item"><svg class="services__tick" viewBox="0 0 14 14" aria-hidden="true"><path d="M2 7.5 L5.5 11 L12 3.5" fill="none" stroke="#fff" stroke-width="2"/></svg>Close in Days</li>
        <li class="services__item"><svg class="services__tick" viewBox="0 0 14 14" aria-hidden="true"><path d="M2 7.5 L5.5 11 L12 3.5" fill="none" stroke="#fff" stroke-width="2"/></svg>No Realtor Fees</li>
        <li class="services__item"><svg class="services__tick" viewBox="0 0 14 14" aria-hidden="true"><path d="M2 7.5 L5.5 11 L12 3.5" fill="none" stroke="#fff" stroke-width="2"/></svg>Renovate &amp; Resell</li>
      </ul>
    </div>
    <div class="services-divider"></div>
    <div class="brand-name">
      <span class="brand-name__mark"></span>
      <span class="brand-name__text"><span>Brightgate</span><span>Holdings</span></span>
    </div>
  </section>

</main>
</body>
</html>
```